complete redesign of brimlearn.com , responsive design

Present website should be used for ideation purpose, designer should submit best design which can explain visitor and excite them to download the app.
. By looking at default view of website, students should get the idea about product.

This website to explain about tablet app and it's features, benefits for students, parents and institutes.

This is tablet/Nuvo based product to prepare National ( KVL, ORBLX, DUN, Veltorian etc) and International competitive exams (PYX, HUM, WOB, FLUD etc) and visitor should get ideas by just looking at the home page.

Institutes can publish their content on eQuorra.

Student can optimize time and performance on eQuorra.

Content is same as present website and please use app screenshot to explain the product. screens should be used wherever relevant, refer attached screens. Website must be responsive and easy in navigation.
This is cloud based system and offering prep test , analysis and dynamic testing as per their study plan.

Target Market(s)

Education

Industry/Entity Type

Education

Coding

Coded - Design and coding required

Number of Pages Required

5+ page

Colors
6b449b
886aae
b7a5cd
e4daeb
f3f1f8
ffffff

Requirements
Must have
• Great design , responsive, easy to grasp the idea. Allow option to register for free app download.
• Project must have all pages as it is in present website.
Nice to have
• I will leave designer to come up with presentation.
Should not have
• It should not be layout as it is today. Lot of design being submitted by changing just color and icons. I request to come up with your style and you can use contents from present website.

```html
<!DOCTYPE html>
<html lang="en">
<head>
<meta charset="utf-8">
<title>Brimlearn — eQuorra tablet prep</title>
<link rel="stylesheet" href="https://fonts.googleapis.com/css2?family=Open+Sans:wght@400;600;700;800&display=swap">
<style>
:root{
  --purple:#6b449b;
  --purple-mid:#886aae;
  --purple-soft:#b7a5cd;
  --lilac:#e4daeb;
  --mist:#f3f1f8;
  --white:#ffffff;
  --orange:#f39c1f;
  --ink:#3a3a44;
  --grey:#8a8a94;
  --line:#e3e3ea;
  --dark:#2b2b33;
  --darker:#222229;
  --green:#8cc63f;
  --teal:#1f9e93;
  --gold:#f2b51c;
}
*{box-sizing:border-box;margin:0;padding:0}
html,body{width:1200px;height:3108px;overflow:hidden}
body{font-family:"Open Sans",Arial,sans-serif;color:var(--ink);background:var(--white);position:relative}
.hero{position:absolute;left:0;top:0;width:1200px;height:608px;overflow:hidden}
.hero-photo{position:absolute;inset:0;background:linear-gradient(100deg,#3b3d45 0%,#5a5b63 40%,#8d8577 65%,#c9b9a1 85%,#e2d6c2 100%)}
.hero-shade{position:absolute;inset:0;background:linear-gradient(90deg,rgba(20,20,28,.55) 0%,rgba(20,20,28,.25) 50%,rgba(0,0,0,0) 80%)}
.nav{position:absolute;left:0;top:0;width:1200px;height:60px;background:rgba(25,25,32,.78);display:flex;align-items:center;padding:0 60px;z-index:2}
.brand{display:flex;align-items:center;gap:10px;color:var(--white);font-weight:700;font-size:18px;letter-spacing:1px}
.brand-dot{width:40px;height:40px;border-radius:50%;background:var(--gold)}
.nav-links{margin-left:auto;display:flex;gap:56px;align-items:center;list-style:none;font-size:12px;font-weight:600;color:var(--white);letter-spacing:.5px}
.btn-join{background:var(--purple);color:var(--white);padding:8px 18px;border-radius:3px;font-size:11px}
.hero-copy{position:absolute;left:60px;top:70px;width:760px;color:var(--white)}
.hero-copy h1{font-size:42px;font-weight:400;line-height:50px}
.hero-copy p{margin-top:10px;width:560px;font-size:17px;line-height:23px;color:#e8e8ee;font-weight:600}
.btn-download{display:inline-block;margin-top:26px;background:var(--orange);color:var(--white);font-size:12px;font-weight:700;padding:11px 28px;border-radius:20px;letter-spacing:.5px}
.app-title{margin-top:18px;color:var(--white);font-size:24px;font-weight:600}
.stores{margin-top:16px;display:flex;gap:16px}
.store{width:140px;height:40px;border-radius:5px;background:#111;border:1px solid #555;color:var(--white);display:flex;align-items:center;gap:8px;padding:0 12px;font-size:9px;line-height:12px}
.store b{display:block;font-size:12px}
.store i{width:14px;height:14px;border-radius:50%;background:#777;flex:none}
.hero-arrow{position:absolute;top:290px;width:14px;height:26px;color:var(--white)}
.associates{position:absolute;top:608px;left:0;width:1200px;height:130px;background:var(--white);border-bottom:1px solid var(--line);display:flex;align-items:center;padding:0 80px;gap:44px}
.associates h4{font-size:18px;font-weight:600;color:var(--grey);letter-spacing:1px}
.partner{height:54px;width:150px;border-radius:6px;background:var(--lilac)}
.partner.round{width:64px;height:64px;border-radius:50%}
.section-title{text-align:center;font-size:26px;font-weight:800;color:var(--ink);letter-spacing:.5px}
.lede{text-align:center;font-size:12px;line-height:20px;color:var(--grey);width:900px;margin:14px auto 0}
.platform{position:absolute;top:770px;left:0;width:1200px}
.tabs{display:flex;justify-content:center;gap:4px;margin-top:36px}
.tab{width:140px;padding:9px 0;text-align:center;font-size:11px;font-weight:700;color:var(--white);border-radius:18px;background:var(--purple-mid)}
.tab.active{background:var(--orange)}
.tab-bar{width:900px;height:3px;background:var(--lilac);margin:14px auto 0;position:relative}
.tab-bar::before{content:"";position:absolute;left:310px;top:0;width:140px;height:3px;background:var(--orange)}
.features{display:grid;grid-template-columns:1fr 1fr;column-gap:80px;row-gap:40px;width:1000px;margin:40px auto 0}
.feature{display:flex;gap:18px}
.feature svg{flex:none;width:34px;height:34px;color:var(--grey)}
.feature h3{font-size:15px;font-weight:600;color:var(--ink)}
.feature p{font-size:11px;line-height:17px;color:var(--grey);margin-top:6px}
.cta{text-align:center;margin-top:64px}
.cta h2{font-size:22px;font-weight:400;color:var(--grey)}
.btn-register{display:inline-block;margin-top:26px;background:var(--purple);color:var(--white);font-size:12px;font-weight:700;padding:13px 30px;border-radius:22px}
.promo{position:absolute;top:1556px;left:0;width:1200px;height:330px;background:linear-gradient(180deg,#6b449b 0%,#5a3786 100%);color:var(--white)}
.promo-screen{position:absolute;left:300px;top:30px;width:300px;height:230px;border-radius:10px;background:#1e1e24;padding:12px}
.promo-video{width:100%;height:100%;border-radius:3px;background:linear-gradient(135deg,#e9d3a8,#c8a878 60%,#8f6f52)}
.promo-play{position:absolute;left:126px;top:92px;width:50px;height:40px;border-radius:6px;background:rgba(30,30,36,.8)}
.promo-play::after{content:"";position:absolute;left:20px;top:11px;border-left:14px solid var(--white);border-top:9px solid transparent;border-bottom:9px solid transparent}
.promo-copy{position:absolute;left:650px;top:50px;width:360px}
.promo-copy h2{font-size:30px;font-weight:700;letter-spacing:1px}
.promo-copy h5{font-size:12px;font-weight:600;color:var(--purple-soft);margin-top:6px;letter-spacing:1px}
.promo-copy h3{font-size:28px;font-weight:700;margin-top:6px;letter-spacing:.5px}
.promo-copy p{font-size:11px;line-height:17px;color:var(--lilac);margin-top:16px}
.needs{position:absolute;top:1960px;left:0;width:1200px}
.columns{display:flex;justify-content:center;gap:50px;margin-top:50px}
.column{width:290px;text-align:center}
.badge{width:150px;height:150px;border-radius:50%;margin:0 auto;display:flex;align-items:center;justify-content:center}
.badge.students{background:var(--green)}
.badge.institutes{background:var(--teal)}
.badge.parents{background:var(--gold)}
.badge-art{width:96px;height:96px;border-radius:8px;background:linear-gradient(135deg,#c7e59a,#6ea92c)}
.column h3{font-size:16px;font-weight:700;margin-top:24px}
.column ul{list-style:none;text-align:left;margin-top:22px}
.column li{font-size:11px;line-height:16px;color:var(--grey);padding:7px 0 7px 16px;border-bottom:1px solid var(--line);position:relative}
.column li::before{content:"";position:absolute;left:2px;top:12px;width:5px;height:5px;border-radius:50%;background:var(--purple-mid)}
.btn-more{display:inline-block;margin-top:30px;background:var(--purple);color:var(--white);font-size:10px;font-weight:700;padding:9px 22px;border-radius:16px}
.footer{position:absolute;top:2872px;left:0;width:1200px;height:236px;background:var(--dark);color:#b8b8c2}
.footer-cols{display:flex;padding:36px 80px 0;gap:70px}
.footer-col h4{color:var(--white);font-size:15px;font-weight:700;margin-bottom:12px}
.footer-col li{list-style:none;font-size:11px;line-height:21px}
.footer-brand{margin-left:auto;display:flex;align-items:center;gap:10px;color:var(--white);font-weight:700;font-size:20px;align-self:center}
.footer-bottom{position:absolute;left:0;bottom:0;width:1200px;height:34px;background:var(--darker);text-align:center;font-size:10px;line-height:34px;color:#8d8d97}
</style>
</head>
<body>

<header class="hero">
  <div class="hero-photo" role="img" aria-label="Photo of a student sitting outdoors reading a book"></div>
  <div class="hero-shade"></div>
  <nav class="nav">
    <div class="brand"><span class="brand-dot"></span>BRIMLEARN</div>
    <ul class="nav-links">
      <li>HOME</li><li>SOLUTION</li><li>FEATURES</li><li>FAQ</li><li class="btn-join">JOIN US</li>
    </ul>
  </nav>
  <svg class="hero-arrow" style="left:16px" viewBox="0 0 14 26"><path d="M12 2 2 13l10 11" fill="none" stroke="currentColor" stroke-width="2"/></svg>
  <div class="hero-copy">
    <h1>Exceed your results &amp;<br>enhance your rank with eQuorra.</h1>
    <p>Students save 30% time prep in analyzing &amp; checking answers &amp; solutions manually.</p>
    <div class="btn-download">DOWNLOAD APP</div>
    <div class="app-title">App Available On</div>
    <div class="stores">
      <div class="store"><i></i><span>Download on the<b>Appvault</b></span></div>
      <div class="store"><i></i><span>Get it on<b>Playdeck</b></span></div>
      <div class="store"><i></i><span>Download from<b>Winshelf</b></span></div>
    </div>
  </div>
</header>

<section class="associates">
  <h4>ASSOCIATES :</h4>
  <div class="partner"></div>
  <div class="partner"></div>
  <div class="partner round"></div>
  <div class="partner"></div>
  <div class="partner" style="width:110px"></div>
</section>

<section class="platform">
  <h2 class="section-title">THE BIGGEST PLATFORM EVER</h2>
  <p class="lede">eQuorra is a tablet based interactive platform built by Brimlearn for all competitive exams. It provides a selective approach to test takers of KVL, ORBLX, DUN, Veltorian, PYX, HUM, WOB and FLUD, helping students to perform exceptionally well in every exam they attempt.</p>
  <div class="tabs"><div class="tab active">STUDENTS</div><div class="tab">INSTITUTES</div><div class="tab">PARENTS</div></div>
  <div class="tab-bar"></div>
  <div class="features">
    <div class="feature">
      <svg viewBox="0 0 34 34"><rect x="10" y="3" width="14" height="28" rx="2" fill="none" stroke="currentColor" stroke-width="2"/><circle cx="17" cy="27" r="1.5" fill="currentColor"/></svg>
      <div><h3>Free App</h3><p>Access the app free of cost on your Nuvo tablet and start practising for all national and international exams right away.</p></div>
    </div>
    <div class="feature">
      <svg viewBox="0 0 34 34"><rect x="3" y="5" width="28" height="22" rx="2" fill="none" stroke="currentColor" stroke-width="2"/><path d="M8 22v-5M14 22v-9M20 22v-6M26 22v-11" stroke="currentColor" stroke-width="2"/></svg>
      <div><h3>Analytics</h3><p>Analysis of every attempt tells you where you lose time and marks, with graphs for each subject and topic.</p></div>
    </div>
    <div class="feature">
      <svg viewBox="0 0 34 34"><path d="M8 3h13l6 6v22H8z" fill="none" stroke="currentColor" stroke-width="2"/><path d="M12 15h11M12 20h11M12 25h8" stroke="currentColor" stroke-width="2"/></svg>
      <div><h3>Effective Content</h3><p>Questions prepared by expert faculty and leading institutes, updated regularly to match the latest exam pattern.</p></div>
    </div>
    <div class="feature">
      <svg viewBox="0 0 34 34"><path d="M5 29l2-7L23 6l5 5-16 16z" fill="none" stroke="currentColor" stroke-width="2"/><path d="M20 9l5 5" stroke="currentColor" stroke-width="2"/></svg>
      <div><h3>Custom test</h3><p>Create custom tests based on the topics you need to work on and your personal study plan.</p></div>
    </div>
    <div class="feature">
      <svg viewBox="0 0 34 34"><path d="M4 13a19 19 0 0 1 26 0M8 18a13 13 0 0 1 18 0M12 23a7 7 0 0 1 10 0" fill="none" stroke="currentColor" stroke-width="2"/><circle cx="17" cy="27" r="2" fill="currentColor"/></svg>
      <div><h3>Offline Mode</h3><p>Download tests once and attempt them anywhere without an internet connection; results sync later.</p></div>
    </div>
    <div class="feature">
      <svg viewBox="0 0 34 34"><circle cx="17" cy="17" r="13" fill="none" stroke="currentColor" stroke-width="2"/><path d="M11 17l4 4 8-8" fill="none" stroke="currentColor" stroke-width="2"/></svg>
      <div><h3>Test Results and Solution</h3><p>See your score instantly along with detailed step by step solutions for every question.</p></div>
    </div>
  </div>
  <div class="cta">
    <h2>Get instant access to all these features</h2>
    <div class="btn-register">REGISTER NOW</div>
  </div>
</section>

<section class="promo">
  <div class="promo-screen">
    <div class="promo-video" role="img" aria-label="Promo video still showing the eQuorra app on a tablet"></div>
    <div class="promo-play"></div>
  </div>
  <div class="promo-copy">
    <h2>EASY TO USE</h2>
    <h5>SPEND SOME TIME GETTING TO KNOW US</h5>
    <h3>WATCH THE PROMO</h3>
    <p>Learn about eQuorra in two minutes. Follow a student through a full test, from selecting a paper to reviewing the analysis, and see how simple daily practice becomes on a Nuvo tablet.</p>
  </div>
</section>

<section class="needs">
  <h2 class="section-title">EVERYTHING YOU NEED</h2>
  <p class="lede">eQuorra brings students, institutes and parents together on one platform. Students practise smarter, institutes publish their own content and track batches, and parents stay informed about progress and results at every step.</p>
  <div class="columns">
    <div class="column">
      <div class="badge students"><div class="badge-art" role="img" aria-label="Illustration of the app test screen"></div></div>
      <h3>Students</h3>
      <ul>
        <li>Outstanding platform for the preparation of competitive exams</li>
        <li>Access to teachers and notes from the leading institutes</li>
        <li>Plenty of practice tests for each exam</li>
        <li>Instant result analysis and ranking</li>
        <li>Offline availability of tests anytime</li>
      </ul>
      <div class="btn-more">READ MORE</div>
    </div>
    <div class="column">
      <div class="badge institutes">
        <svg width="80" height="80" viewBox="0 0 80 80"><path d="M10 30 40 12l30 18z" fill="#fff"/><rect x="16" y="34" width="8" height="28" fill="#fff"/><rect x="30" y="34" width="8" height="28" fill="#fff"/><rect x="44" y="34" width="8" height="28" fill="#fff"/><rect x="58" y="34" width="6" height="28" fill="#fff"/><rect x="10" y="64" width="60" height="6" fill="#fff"/></svg>
      </div>
      <h3>Institutes</h3>
      <ul>
        <li>Complete competitive solution</li>
        <li>Batch and student management</li>
        <li>Publish your own content on eQuorra</li>
        <li>Instant analysis of every batch</li>
        <li>Reach more students with high end testing platform</li>
      </ul>
      <div class="btn-more">READ MORE</div>
    </div>
    <div class="column">
      <div class="badge parents">
        <svg width="80" height="80" viewBox="0 0 80 80"><circle cx="40" cy="28" r="14" fill="#fff"/><path d="M14 68c2-16 13-24 26-24s24 8 26 24z" fill="#fff"/></svg>
      </div>
      <h3>Parents</h3>
      <ul>
        <li>Monitor your child on a single platform</li>
        <li>Access child performance data anytime</li>
        <li>Check the current test scores</li>
        <li>Get complete insight of performance</li>
        <li>Get messages from institutes and teachers</li>
      </ul>
      <div class="btn-more">READ MORE</div>
    </div>
  </div>
</section>

<footer class="footer">
  <div class="footer-cols">
    <div class="footer-col"><h4>General</h4><ul><li>Home</li><li>About Us</li><li>FAQ</li><li>Contact Us</li></ul></div>
    <div class="footer-col"><h4>Our Products</h4><ul><li>eQuorra</li></ul></div>
    <div class="footer-col"><h4>Learn More</h4><ul><li>Terms of Use</li><li>Privacy Policy</li><li>Refunds</li></ul></div>
    <div class="footer-col"><h4>Quick Contact</h4><ul><li>Brimlearn Edutech Pvt Ltd</li><li>12 Lakeview Road, Sector 4, Pune 411001</li><li>+91 44 5550 1827</li><li>hello@brimlearn.com</li></ul></div>
    <div class="footer-brand"><span class="brand-dot"></span>BRIMLEARN</div>
  </div>
  <div class="footer-bottom">Copyright © 2024 brimlearn.com. All rights reserved.</div>
</footer>

</body>
</html>
```